Heron valley RV Resort business card

I need a design card for the logo I just had made on here. I will provide it and please make some cool designs, thank you.

I would like the card to have
- phone number (865-318-2967)
- email ( heronvalleyrv@pinemail.com)
- address to the park ( 5186 Quarry Gate Loop rd, Maryville, TN) ZIP: 37429
on the back for double sided id like some lines for writing on. thanks

please follow the logo we provided in the files, I can provide the photoshop file if you need it.

please note this is in the Smokey mountains of Tennessee

Target Market(s)

cabin/rv rentals

Industry/Entity Type

rv/campground/cabin rentals

Contact Information for Business Card

address/email/phone number I added details in brief

Requirements
Must have
• on the back add a bear or something cool

```html
<!DOCTYPE html>
<html lang="en">
<head>
<meta charset="utf-8">
<title>Heron valley RV Resort – Business Card</title>
<link rel="stylesheet" href="https://fonts.googleapis.com/css2?family=EB+Garamond:wght@400;500&display=swap">
<style>
  :root {
    --backdrop: #e9e6e1;
    --card: #ffffff;
    --card-shade: #f1f1f1;
    --ink: #2b2b2b;
    --accent: #e8703f;
    --forest: #121a16;
    --bear-fill: #f0a27f;
  }
  * { box-sizing: border-box; margin: 0; padding: 0; }
  html, body {
    width: 1200px; height: 900px; overflow: hidden;
    background: var(--backdrop);
    font-family: "EB Garamond", Georgia, serif;
    color: var(--ink);
  }
  .stage {
    width: 1200px; height: 900px;
    display: flex; flex-direction: column; align-items: center; justify-content: center;
    gap: 40px;
  }
  .card {
    position: relative;
    width: 660px; height: 377px;
    background: linear-gradient(120deg, var(--card) 55%, var(--card-shade));
    overflow: hidden;
    box-shadow: 0 6px 18px rgba(0,0,0,.18);
  }
  .forest {
    position: absolute; left: 0; bottom: 0;
    width: 660px; height: 377px;
  }

  /* back side */
  .bear-art {
    position: absolute; left: 70px; top: 120px;
    width: 170px; height: 130px;
    background: var(--bear-fill);
    border-radius: 40px 60px 20px 30px;
  }
  .write-lines { position: absolute; left: 0; top: 0; width: 660px; height: 377px; }
  .write-lines line {
    stroke: var(--accent); stroke-width: 2; stroke-dasharray: 2 4;
  }

  /* front side */
  .brand {
    position: absolute; left: 50px; top: 100px;
    display: flex; align-items: center; gap: 14px;
    width: 230px;
  }
  .brand-dot {
    flex: none; width: 22px; height: 22px; border-radius: 50%;
    background: var(--accent);
  }
  .brand-name {
    font-size: 27px; font-weight: 500; line-height: 1.1;
    color: var(--ink);
  }
  .contact {
    position: absolute; left: 295px; top: 66px;
    list-style: none;
    display: flex; flex-direction: column; gap: 20px;
    font-size: 17px;
  }
  .contact li { display: flex; align-items: center; gap: 10px; white-space: nowrap; }
  .contact svg { width: 16px; height: 16px; flex: none; fill: var(--accent); }
</style>
</head>
<body>
<main class="stage">

  <section class="card card-back" aria-label="Back of card with writing lines">
    <div class="bear-art" role="img" aria-label="Orange line illustration of a walking bear"></div>
    <svg class="write-lines" viewBox="0 0 660 377" aria-hidden="true">
      <line x1="250" y1="100" x2="600" y2="100"/>
      <line x1="250" y1="160" x2="600" y2="160"/>
      <line x1="70"  y1="252" x2="600" y2="252"/>
    </svg>
    <svg class="forest" viewBox="0 0 660 377" role="img" aria-label="Silhouette of a pine forest along the lower edge">
      <polygon fill="var(--forest)" points="0,377 0,305 200,332 380,305 500,278 580,262 625,240 645,175 660,140 660,377"/>
    </svg>
  </section>

  <section class="card card-front" aria-label="Front of card">
    <div class="brand">
      <span class="brand-dot"></span>
      <span class="brand-name">Heron valley RV Resort</span>
    </div>
    <ul class="contact">
      <li>
        <svg viewBox="0 0 24 24" aria-hidden="true"><path d="M6.6 10.8a15 15 0 0 0 6.6 6.6l2.2-2.2a1 1 0 0 1 1-.25 11.4 11.4 0 0 0 3.6.6 1 1 0 0 1 1 1V20a1 1 0 0 1-1 1A17 17 0 0 1 3 4a1 1 0 0 1 1-1h3.5a1 1 0 0 1 1 1c0 1.25.2 2.45.6 3.6a1 1 0 0 1-.25 1z"/></svg>
        865-318-2967
      </li>
      <li>
        <svg viewBox="0 0 24 24" aria-hidden="true"><path d="M3 5h18a1 1 0 0 1 1 1v12a1 1 0 0 1-1 1H3a1 1 0 0 1-1-1V6a1 1 0 0 1 1-1zm9 7 8-5H4z"/></svg>
        heronvalleyrv@pinemail.com
      </li>
      <li>
        <svg viewBox="0 0 24 24" aria-hidden="true"><path d="M12 2a7 7 0 0 1 7 7c0 5-7 13-7 13S5 14 5 9a7 7 0 0 1 7-7zm0 4.5A2.5 2.5 0 1 0 12 11.5 2.5 2.5 0 0 0 12 6.5z"/></svg>
        5186 Quarry Gate Loop rd, Maryville, TN
      </li>
    </ul>
    <svg class="forest" viewBox="0 0 660 377" role="img" aria-label="Silhouette of a pine forest along the lower edge">
      <polygon fill="var(--forest)" points="0,377 0,305 200,332 380,305 500,278 580,262 625,240 645,175 660,140 660,377"/>
    </svg>
  </section>

</main>
</body>
</html>
```